Need Landing Page for Data Security Company

Need a new landing page (PSD) for our data security company (www.korvalim.com). We specialize in selling patented hard drive destruction machines that guarantee the data on your hard drives are unrecoverable. We have several large clients such as Trellio, Quibblr and Marquell just to name a few. Really want to have a landing page that sticks out.

Attached is a one pager we use just for emailing clients. We do not want the landing page to look like this. This is just for content to read. The landing page needs

Target Market(s)

Government, business corporations, IT decision makers. Not every day user

Industry/Entity Type

It Company

Number of Pages Required

1 page

Font styles to use
Other font styles liked:
• Match Current Website

Requirements
Must have
• Its a landing page so it needs a Contact us Section at the very top!!!
• Need to be a very attractive landing page.. Would like a mix of showcasing our products and also having some client list to show our bigger name clients (trellio, marquell, quibblr)
• Landing page needs to use the same color/style schema as current website. Also will be using the same menu structure as what exists today.
• www.korvalim.com
Nice to have
• Maybe some vidmora videos of our products?

```html
<!DOCTYPE html>
<html lang="en">
<head>
<meta charset="utf-8">
<title>Korvalim – Innovative Solutions</title>
<link href="https://fonts.googleapis.com/css2?family=Open+Sans:wght@400;600;700&family=Raleway:wght@400;600;700;800&display=swap" rel="stylesheet">
<style>
:root{
  --green:#8cc152;
  --green-dark:#6fa236;
  --black:#111;
  --ink:#333;
  --muted:#777;
  --light:#f4f4f4;
  --footer:#2e2e2e;
  --footer-text:#bdbdbd;
  --white:#fff;
}
*{box-sizing:border-box;margin:0;padding:0}
html,body{width:1200px;height:2428px;overflow:hidden}
body{font-family:"Open Sans",Arial,sans-serif;color:var(--ink);background:var(--white);font-size:13px;line-height:1.6}

/* header */
.site-header{height:72px;background:var(--black);display:flex;align-items:center;justify-content:space-between;padding:0 40px 0 30px}
.brand{display:flex;flex-direction:column;line-height:1}
.brand-name{font-family:"Raleway",sans-serif;font-weight:700;font-size:34px;color:var(--green)}
.brand-tag{font-size:9px;color:#aaa;letter-spacing:.5px;margin-top:3px;padding-left:2px}
.main-nav{display:flex;gap:34px}
.main-nav a{color:#ddd;text-decoration:none;font-size:12px;font-weight:600;letter-spacing:.5px}
.main-nav a.active{color:var(--green)}

/* hero */
.hero{position:relative;height:616px;overflow:hidden;
  background:linear-gradient(90deg,#3c4046 0%,#575c63 14%,#8e949a 28%,#c9cdd0 42%,#e4e6e7 58%,#eef0f0 100%)}
.hero-photo{position:absolute;inset:0;
  background:linear-gradient(180deg,rgba(255,255,255,.35) 0%,rgba(255,255,255,0) 35%,rgba(40,44,50,.18) 100%)}
.hero-copy{position:absolute;right:60px;top:290px;text-align:right}
.hero-copy h1{font-family:"Raleway",sans-serif;font-weight:800;font-size:48px;color:var(--green);line-height:1}
.hero-copy h2{font-family:"Raleway",sans-serif;font-weight:700;font-size:30px;color:var(--ink);margin-top:10px}
.hero-copy p{font-size:20px;color:var(--ink);margin-top:6px}
.hero-arrows{position:absolute;right:56px;bottom:32px;display:flex;gap:4px}
.hero-arrows span{width:32px;height:32px;background:var(--black);display:flex;align-items:center;justify-content:center}

/* welcome */
.welcome{height:212px;text-align:center;padding:30px 110px 0}
.section-title{font-family:"Raleway",sans-serif;font-weight:700;font-size:26px;color:var(--ink)}
.section-title em{font-style:normal;color:var(--green)}
.title-rule{width:70px;height:3px;background:var(--green);margin:10px auto 18px}
.welcome p{font-size:12px;color:var(--muted);line-height:1.8}

/* green band */
.process{height:480px;background:var(--green);text-align:center;padding-top:58px;color:var(--white)}
.process h2{font-family:"Raleway",sans-serif;font-weight:700;font-size:40px;line-height:1.1}
.process h3{font-family:"Raleway",sans-serif;font-weight:600;font-size:27px;color:#2f3b22;margin-top:6px}
.steps{display:flex;justify-content:center;align-items:flex-start;margin-top:50px}
.step{width:260px;display:flex;flex-direction:column;align-items:center}
.step-image{width:156px;height:156px;border-radius:50%;border:6px solid var(--white);box-shadow:0 4px 12px rgba(0,0,0,.25)}
.step-image.disks{background:linear-gradient(135deg,#ffffff 0%,#d6d8da 30%,#8d9196 60%,#3f4247 100%)}
.step-image.machine{background:linear-gradient(160deg,#ffffff 0%,#f1f2f2 45%,#b9bcbe 80%,#7d8084 100%)}
.step-image.debris{background:linear-gradient(150deg,#8a8d92 0%,#4a4d52 40%,#222326 75%,#0f1011 100%)}
.step p{font-size:14px;font-weight:600;color:#26311c;margin-top:16px;line-height:1.4}
.step-arrow{margin-top:68px}

/* products */
.products{height:420px;padding:24px 30px 0}
.products-head{display:flex;justify-content:space-between;align-items:center;border-bottom:1px solid #ddd;padding-bottom:12px}
.products-head h2{font-family:"Raleway",sans-serif;font-weight:700;font-size:20px}
.products-head h2 em{font-style:normal;color:var(--green)}
.slider-nav{display:flex;gap:2px}
.slider-nav span{width:20px;height:18px;background:#555}
.product-row{display:flex;gap:14px;margin-top:28px}
.product-card{flex:1;box-shadow:0 2px 6px rgba(0,0,0,.15)}
.product-image{height:176px}
.product-image.p1{background:linear-gradient(90deg,#e9eaeb 0%,#3a3c40 38%,#2b2c2f 52%,#cfd1d3 70%,#f3f3f3 100%)}
.product-image.p2{background:linear-gradient(180deg,#f5f5f5 0%,#e1e3e4 55%,#9ea2a6 100%)}
.product-image.p3{background:linear-gradient(90deg,#f4f4f4 0%,#d4d6d8 40%,#2f3034 62%,#c8cacc 80%,#efefef 100%)}
.product-image.p4{background:linear-gradient(180deg,#fafafa 0%,#e4e6e6 50%,#a8acaf 100%)}
.product-card h4{background:#3a3a3a;color:var(--white);font-size:11px;font-weight:600;text-align:center;padding:9px 0;letter-spacing:.5px}

/* feature */
.feature{height:228px;display:flex;gap:40px;padding:0 46px 0 92px}
.feature-copy{flex:1}
.feature-copy h2{font-family:"Raleway",sans-serif;font-weight:700;font-size:20px;color:var(--green)}
.feature-copy p{font-size:12px;color:var(--muted);margin-top:12px;line-height:1.75}
.btn-outline{display:inline-block;margin-top:18px;border:1px solid #999;color:#555;font-size:11px;padding:6px 14px;border-radius:3px}
.video{width:412px;height:212px;position:relative;border:1px solid #ccc;
  background:linear-gradient(90deg,#f6f6f6 0%,#dfe1e2 40%,#6d7176 70%,#d9dbdc 100%)}
.video-play{position:absolute;left:176px;top:78px;width:60px;height:42px;border-radius:8px;background:rgba(40,40,40,.85);display:flex;align-items:center;justify-content:center}
.video-bar{position:absolute;left:0;right:0;bottom:0;height:26px;background:#1b1b1b;display:flex;align-items:center;padding:0 10px;gap:10px}
.video-bar .track{flex:1;height:3px;background:#555}
.video-bar .track i{display:block;width:4%;height:3px;background:var(--green)}

/* clients */
.clients{height:112px;text-align:center;padding-top:10px}
.clients h5{font-size:12px;font-weight:700;color:var(--green);letter-spacing:.5px}
.client-row{display:flex;justify-content:space-around;align-items:center;margin-top:18px;padding:0 70px}
.client{font-weight:700;font-size:22px;color:#444;display:flex;align-items:center;gap:8px}
.client .dot{width:22px;height:22px;background:#444}
.badge{width:56px;height:44px;background:#555}
.badge.round{border-radius:50%;width:46px;height:46px}

/* footer */
.site-footer{height:252px;background:var(--footer);color:var(--footer-text);display:flex;gap:40px;padding:34px 60px 0}
.footer-col{flex:1;font-size:11.5px;line-height:1.75}
.footer-col h6{font-size:12px;font-weight:700;color:var(--white);letter-spacing:.5px;margin-bottom:14px}
.field{height:28px;background:var(--white);border-radius:3px;margin-top:12px;color:#999;font-size:11px;padding:5px 10px}
.btn-dark{display:inline-block;background:#111;color:var(--white);font-size:10px;font-weight:700;padding:6px 14px;margin-top:10px}
.social{display:flex;align-items:center;gap:10px;margin-bottom:12px}
.social .circle{width:22px;height:22px;border-radius:50%;background:#555}
.copyright{height:36px;background:#0c0c0c;color:#999;font-size:11px;display:flex;align-items:center;justify-content:center;position:relative}
.copyright .up{position:absolute;right:40px}
</style>
</head>
<body>

<header class="site-header">
  <div class="brand">
    <span class="brand-name">Korvalim</span>
    <span class="brand-tag">Innovative Solutions Company</span>
  </div>
  <nav class="main-nav">
    <a class="active" href="#">HOME</a>
    <a href="#">ABOUT US</a>
    <a href="#">PRODUCTS</a>
    <a href="#">SERVICES</a>
    <a href="#">COMPLIANCE</a>
    <a href="#">BLOG</a>
    <a href="#">CONTACT</a>
  </nav>
</header>

<section class="hero">
  <div class="hero-photo" role="img" aria-label="Business team in a bright office, a man in a dark suit in front with colleagues around a laptop"></div>
  <div class="hero-copy">
    <h1>KORVALIM</h1>
    <h2>INNOVATIVE SOLUTIONS</h2>
    <p>Specializing in technology solutions</p>
  </div>
  <div class="hero-arrows">
    <span><svg width="10" height="12" viewBox="0 0 10 12"><path d="M8 1 2 6l6 5" fill="none" stroke="#fff" stroke-width="2"/></svg></span>
    <span><svg width="10" height="12" viewBox="0 0 10 12"><path d="M2 1l6 5-6 5" fill="none" stroke="#fff" stroke-width="2"/></svg></span>
  </div>
</section>

<section class="welcome">
  <h2 class="section-title">WELCOME TO <em>KORVALIM</em></h2>
  <div class="title-rule"></div>
  <p>Our company is an innovator in data security, introducing unique and patented data destruction products. Hard drive data destruction such as the DataCrush, the DataCrush Compact, and the DataCrush 320. These products were engineered in response to the rapid growth of information technology and the inherent risk of data breaches. Federal security agencies have issued strict standards that government and private entities alike must follow to protect sensitive information from data security breaches.</p>
</section>

<section class="process">
  <h2>Korvalim Innovative Solutions</h2>
  <h3>The Only Hassle Free Automated Crushing System</h3>
  <div class="steps">
    <div class="step">
      <div class="step-image disks" role="img" aria-label="Computer hard drives and storage media"></div>
      <p>Computer Storage Media</p>
    </div>
    <svg class="step-arrow" width="40" height="20" viewBox="0 0 40 20"><path d="M0 10h34M26 3l8 7-8 7" fill="none" stroke="#fff" stroke-width="2"/></svg>
    <div class="step">
      <div class="step-image machine" role="img" aria-label="DataCrush destroyer machine"></div>
      <p>Korvalim DataCrush Destroyer</p>
    </div>
    <svg class="step-arrow" width="40" height="20" viewBox="0 0 40 20"><path d="M0 10h34M26 3l8 7-8 7" fill="none" stroke="#fff" stroke-width="2"/></svg>
    <div class="step">
      <div class="step-image debris" role="img" aria-label="Pile of crushed hard drive debris"></div>
      <p>Crushed, Mangled and Rendered<br>Unreadable Storage Media</p>
    </div>
  </div>
</section>

<section class="products">
  <div class="products-head">
    <h2><em>KORVALIM</em> PRODUCTS</h2>
    <div class="slider-nav"><span></span><span></span></div>
  </div>
  <div class="product-row">
    <article class="product-card"><div class="product-image p1" role="img" aria-label="Woman in dark clothing presenting the DataCrush Compact"></div><h4>DATACRUSH COMPACT</h4></article>
    <article class="product-card"><div class="product-image p2" role="img" aria-label="DataCrush machine on a desk"></div><h4>DATACRUSH</h4></article>
    <article class="product-card"><div class="product-image p3" role="img" aria-label="Woman standing beside the DataCrush 320"></div><h4>DATACRUSH 320</h4></article>
    <article class="product-card"><div class="product-image p4" role="img" aria-label="DataCrush V320 unit"></div><h4>DATACRUSH V320</h4></article>
  </div>
</section>

<section class="feature">
  <div class="feature-copy">
    <h2>DATACRUSH</h2>
    <p>The DataCrush is a desktop data destruction solution standing only 20 inches tall and 17 inches wide. When a computer hard drive is fed into the DataCrush, its patented crushing gears deliver over 40,000 pounds of force to the vulnerable platters and circuit boards of the drive. In less than a minute, the hard drive is crushed, mangled and discharged into a debris collection bin. The entire process is completely hands off.</p>
    <span class="btn-outline">Read more</span>
  </div>
  <div class="video" role="img" aria-label="Product video of the DataCrush machine">
    <div class="video-play"><svg width="18" height="20" viewBox="0 0 18 20"><path d="M2 2l14 8-14 8z" fill="#fff"/></svg></div>
    <div class="video-bar">
      <svg width="10" height="12" viewBox="0 0 10 12"><path d="M1 1l8 5-8 5z" fill="#fff"/></svg>
      <div class="track"><i></i></div>
    </div>
  </div>
</section>

<section class="clients">
  <h5>OUR CLIENTS INCLUDE</h5>
  <div class="client-row">
    <div class="badge" aria-label="Partner badge"></div>
    <div class="badge round" aria-label="Agency badge"></div>
    <div class="client">trellio</div>
    <div class="client"><span class="dot"></span></div>
    <div class="client">Veranth</div>
    <div class="client">marquell</div>
  </div>
</section>

<footer class="site-footer">
  <div class="footer-col">
    <h6>NEWSLETTER SIGN UP</h6>
    <p>Sign up for our latest news and product updates from our team.</p>
    <div class="field">Email address</div>
    <span class="btn-dark">SUBSCRIBE</span>
  </div>
  <div class="footer-col">
    <h6>ABOUT US</h6>
    <p>In the era of data breaches, we have provided secure hard drive destruction for over a decade. Our machines deliver peace of mind to clients with critical data.</p>
  </div>
  <div class="footer-col">
    <h6>GET IN TOUCH</h6>
    <p>Address: 75 Harbor Mill Lane, Suite 4</p>
    <p>Ph: (555) 014-2290</p>
    <p>Fax: 555 014 2291</p>
    <p>Email: info@korvalim.com</p>
  </div>
  <div class="footer-col">
    <h6>FOLLOW US ON</h6>
    <div class="social"><span class="circle"></span>Trellio</div>
    <div class="social"><span class="circle"></span>Quibblr</div>
    <div class="social"><span class="circle"></span>Snapwell</div>
  </div>
</footer>
<div class="copyright">Copyright © 2015. All Rights.<span class="up">Up</span></div>

</body>
</html>
```